Dorvel519 Smoke shop and Wine Store

DORVEL SMOKE SHOP & WINE INC

Smoke shop, Bill payments, unlock phones,Cellphones, Cellphone accessories and repair.
ADDRESS:
519 Harlow Ave11472Brooklyn, NY
phone # 3470182947
Mobile # 3470264813
E-mail: Dorvel5196@mailbrisk.com
Instagram: DORVELSMOKESHOP

we sell hookah and all hookah accessories and tobaccos. E-cigarettes, vapes, E-juice, vapes parts and replacements, unlocked phones, bill payments and international to-ups,

Target Market(s)

SMOKE sHOPS
Cell phones market

Industry/Entity Type

Shop

Contact Information for Business Card

Tarek Homsi
3470182947
3470264813

Smoke Shop - Unlocked phones - Phone Accessories - phone repair - bill payments - unlock services.

Font styles to use
Decorative

Requirements
Must have
• - attractive colors and designs on the business card.
• - graphics
Nice to have
• Cellphone pics and graphs

```html
<!DOCTYPE html>
<html lang="en">
<head>
<meta charset="utf-8">
<title>Dorvel Smoke Shop &amp; Wine – Business Card</title>
<link rel="stylesheet" href="https://fonts.googleapis.com/css2?family=Montserrat:wght@800&family=Raleway:wght@400;500;600;700;800&display=swap">
<style>
  :root {
    --ink-black: #000000;
    --glow-red: #8a1a14;
    --glow-brown: #3b1a12;
    --accent-yellow: #ffc60b;
    --brand-red: #c8262c;
    --text-white: #e6e6e6;
    --tagline-grey: #8c8c92;
  }
  html, body {
    margin: 0;
    padding: 0;
    width: 1200px;
    height: 695px;
    overflow: hidden;
    background: var(--ink-black);
  }
  .card {
    position: relative;
    width: 1200px;
    height: 695px;
    overflow: hidden;
    background:
      radial-gradient(ellipse 640px 390px at 600px 340px,
        var(--glow-red) 0%, var(--glow-brown) 55%, var(--ink-black) 100%);
    font-family: "Raleway", sans-serif;
    color: var(--text-white);
  }
  .brand {
    position: absolute;
    left: 118px;
    top: 215px;
    width: 390px;
  }
  .brand-name {
    font-family: "Raleway", sans-serif;
    font-weight: 700;
    font-size: 104px;
    line-height: 1;
    color: var(--brand-red);
    letter-spacing: 1px;
  }
  .brand-tagline {
    margin-top: 22px;
    font-weight: 500;
    font-size: 31px;
    color: var(--tagline-grey);
    letter-spacing: 0.5px;
    white-space: nowrap;
  }
  .divider {
    position: absolute;
    left: 581px;
    top: 41px;
    width: 4px;
    height: 406px;
    background: var(--accent-yellow);
  }
  .address {
    position: absolute;
    left: 647px;
    top: 44px;
    font-weight: 400;
    font-size: 38px;
    line-height: 51px;
    letter-spacing: 0.5px;
  }
  .contact-name {
    position: absolute;
    left: 722px;
    top: 205px;
    font-weight: 800;
    font-size: 42px;
    color: var(--accent-yellow);
  }
  .contact-list {
    position: absolute;
    left: 678px;
    top: 266px;
    margin: 0;
    padding: 0;
    list-style: none;
  }
  .contact-item {
    display: flex;
    align-items: center;
    height: 46px;
    font-weight: 400;
    font-size: 33px;
    letter-spacing: 0.3px;
    white-space: nowrap;
  }
  .contact-icon {
    width: 34px;
    height: 34px;
    margin-right: 14px;
    flex: none;
  }
  .services {
    position: absolute;
    left: 112px;
    top: 497px;
    font-family: "Montserrat", sans-serif;
    font-weight: 800;
    font-size: 44px;
    line-height: 55px;
    color: var(--text-white);
    letter-spacing: 0.3px;
    white-space: nowrap;
  }
  .services .hl { color: var(--accent-yellow); }
</style>
</head>
<body>
<main class="card">
  <section class="brand">
    <div class="brand-name">Dorvel</div>
    <div class="brand-tagline">SMOKE SHOP &amp; WINE</div>
  </section>

  <div class="divider"></div>

  <address class="address" style="font-style:normal">
    519 Harlow Ave<br>11472 Brooklyn<br>NY
  </address>

  <div class="contact-name">Tarek Homsi</div>

  <ul class="contact-list">
    <li class="contact-item">
      <svg class="contact-icon" viewBox="0 0 34 34" aria-hidden="true">
        <circle cx="17" cy="17" r="14" fill="none" stroke="#ffc60b" stroke-width="2.4"/>
        <path d="M11.5 9.5c1-.8 2-.6 2.6.4l1.4 2.4c.4.8.2 1.6-.5 2.1l-1 .7c.8 2 2.3 3.6 4.3 4.6l.8-1c.5-.7 1.4-.8 2.1-.4l2.3 1.5c.9.6 1 1.7.3 2.6-1.3 1.6-3.2 2-5 1.2-3.9-1.8-6.7-4.8-8.2-8.7-.6-1.8-.2-3.9.9-5.4z" fill="#ffc60b"/>
      </svg>
      347 018-2947
    </li>
    <li class="contact-item">
      <svg class="contact-icon" viewBox="0 0 34 34" aria-hidden="true">
        <rect x="10" y="3.5" width="14" height="27" rx="2.5" fill="none" stroke="#ffc60b" stroke-width="2.4"/>
        <line x1="10" y1="24" x2="24" y2="24" stroke="#ffc60b" stroke-width="2"/>
        <circle cx="17" cy="27.3" r="1.3" fill="#ffc60b"/>
      </svg>
      347 026-4813
    </li>
    <li class="contact-item">
      <svg class="contact-icon" viewBox="0 0 34 34" aria-hidden="true">
        <rect x="3" y="8" width="28" height="19" fill="none" stroke="#ffc60b" stroke-width="2.2"/>
        <path d="M3 8l14 11 14-11M3 27l10.5-10M31 27L20.5 17" fill="none" stroke="#ffc60b" stroke-width="2"/>
      </svg>
      Dorvel5196@mailbrisk.com
    </li>
    <li class="contact-item">
      <svg class="contact-icon" viewBox="0 0 34 34" aria-hidden="true">
        <rect x="4" y="4" width="26" height="26" fill="none" stroke="#ffc60b" stroke-width="2.6"/>
      </svg>
      DORVELSMOKESHOP
    </li>
  </ul>

  <p class="services" style="margin:0">
    <span class="hl">SMOKE</span> SHOP<span class="hl">.</span> <span class="hl">BILL</span> PAYMENTS<span class="hl">.</span><br>
    <span class="hl">UNLOCK</span> PHONES<span class="hl">. CELLPHONES.</span><br>
    CELLPHONE <span class="hl">ACCESSORIES</span> AND <span class="hl">REPAIR</span>
  </p>
</main>
</body>
</html>
```